Save our Business Card - We need your help

We need a fresh look on our business cards. We like it as it is, but it's not quite getting the 'wow' effect that we desire.
We're a tech startup building a cloud based solution for retailers consisting of Point of Sale, Inventory management and CRM.
The design should communicate a sense of a company that cares about the little things, design and relationships.
You can have a look at our website www.tillnest.com to get a feel for what we're like. Please feel free to message us for any further clarification
Target Market(s)
Our Customers are retail busines owners, cafe owners, other startups etc.
Industry/Entity Type
Building
Colors
Designer to choose colors to be used in the design.
Look and feel
Each slider illustrates characteristics of the customer's brand and the style your logo design should communicate.

```html
<!DOCTYPE html>
<html lang="en">
<head>
<meta charset="utf-8">
<title>TillNest Business Card</title>
<link rel="stylesheet" href="https://fonts.googleapis.com/css2?family=Open+Sans:wght@700&family=Questrial&display=swap">
<style>
  :root {
    --page-bg: #ffffff;
    --card-bg: #000000;
    --gloss: rgba(255, 255, 255, 0.09);
    --brand-orange: #f7931e;
    --rule-light: #d9d9d9;
    --text-light: #ffffff;
    --text-muted: #9a9a9a;
    --icon-bg: #b3b3b3;
    --icon-ink: #1a1a1a;
  }
  html, body {
    margin: 0;
    padding: 0;
    overflow: hidden;
  }
  body {
    width: 1091px;
    height: 1200px;
    background: var(--page-bg);
    position: relative;
  }
  .card {
    position: absolute;
    left: 235px;
    width: 610px;
    height: 350px;
    background: var(--card-bg);
    border-radius: 0 66px 0 66px;
    box-shadow: 14px 16px 18px rgba(0, 0, 0, 0.45);
    overflow: hidden;
  }
  .card::before {
    content: "";
    position: absolute;
    inset: 0;
    background: linear-gradient(115deg, transparent 0 28%, var(--gloss) 28% 48%, transparent 75%);
    pointer-events: none;
  }
  .card--front { top: 201px; }
  .card--back { top: 638px; }

  .brand {
    position: absolute;
    left: 114px;
    top: 122px;
    display: flex;
    align-items: center;
    gap: 16px;
  }
  .brand__mark {
    width: 86px;
    height: 86px;
    background: var(--brand-orange);
  }
  .brand__name {
    font-family: "Open Sans", sans-serif;
    font-weight: 700;
    font-size: 60px;
    letter-spacing: -1px;
    color: var(--brand-orange);
  }
  .brand__rule {
    position: absolute;
    left: 46px;
    top: 250px;
    width: 518px;
    height: 2px;
    background: linear-gradient(90deg, transparent, var(--rule-light) 20%, var(--rule-light) 80%, transparent);
  }

  .holder {
    position: absolute;
    right: 26px;
    top: 22px;
    text-align: right;
    font-family: "Questrial", sans-serif;
  }
  .holder__name {
    font-size: 29px;
    color: var(--text-light);
    line-height: 1.2;
  }
  .holder__title {
    font-size: 19px;
    color: var(--text-muted);
    margin-top: 2px;
  }
  .contact-icons {
    position: absolute;
    left: 24px;
    top: 122px;
  }
</style>
</head>
<body>
  <section class="card card--front">
    <div class="brand">
      <div class="brand__mark"></div>
      <span class="brand__name">TillNest</span>
    </div>
    <div class="brand__rule"></div>
  </section>

  <section class="card card--back">
    <div class="holder">
      <div class="holder__name">Card Holder</div>
      <div class="holder__title">(Title)</div>
    </div>

    <svg class="contact-icons" width="100" height="200" viewBox="0 0 100 200" aria-label="Contact icons">
      <!-- mobile -->
      <g transform="translate(31,32)">
        <circle r="29" fill="var(--icon-bg)"/>
        <rect x="-10" y="-15" width="20" height="30" rx="3" fill="var(--icon-ink)"/>
        <rect x="-7" y="-12" width="14" height="7" fill="var(--icon-bg)"/>
        <g fill="var(--icon-bg)">
          <rect x="-7" y="-2" width="3" height="3"/><rect x="-1.5" y="-2" width="3" height="3"/><rect x="4" y="-2" width="3" height="3"/>
          <rect x="-7" y="3" width="3" height="3"/><rect x="-1.5" y="3" width="3" height="3"/><rect x="4" y="3" width="3" height="3"/>
          <rect x="-7" y="8" width="3" height="3"/><rect x="-1.5" y="8" width="3" height="3"/><rect x="4" y="8" width="3" height="3"/>
        </g>
      </g>
      <!-- desk phone -->
      <g transform="translate(62,77)">
        <circle r="29" fill="var(--icon-bg)"/>
        <path d="M-17 -8 Q0 -20 17 -8 L14 -3 L8 -5 L8 -9 Q0 -12 -8 -9 L-8 -5 L-14 -3 Z" fill="var(--icon-ink)"/>
        <rect x="-14" y="-2" width="28" height="18" rx="2" fill="var(--icon-ink)"/>
        <g fill="var(--icon-bg)">
          <rect x="-9" y="1" width="4" height="3"/><rect x="-2" y="1" width="4" height="3"/><rect x="5" y="1" width="4" height="3"/>
          <rect x="-9" y="6" width="4" height="3"/><rect x="-2" y="6" width="4" height="3"/><rect x="5" y="6" width="4" height="3"/>
          <rect x="-9" y="11" width="4" height="3"/><rect x="-2" y="11" width="4" height="3"/><rect x="5" y="11" width="4" height="3"/>
        </g>
      </g>
      <!-- envelope -->
      <g transform="translate(31,124)">
        <circle r="29" fill="var(--icon-bg)"/>
        <rect x="-17" y="-11" width="34" height="22" fill="#f2f2f2" stroke="var(--icon-ink)" stroke-width="2"/>
        <path d="M-17 -11 L0 3 L17 -11 M-17 11 L-5 -1 M17 11 L5 -1" fill="none" stroke="var(--icon-ink)" stroke-width="2"/>
      </g>
      <!-- globe -->
      <g transform="translate(62,172)">
        <circle r="29" fill="var(--icon-bg)"/>
        <g fill="none" stroke="var(--icon-ink)" stroke-width="2">
          <circle r="14"/>
          <ellipse rx="6" ry="14"/>
          <line x1="-14" y1="0" x2="14" y2="0"/>
          <line x1="0" y1="-14" x2="0" y2="14"/>
          <path d="M-12 -7 H12 M-12 7 H12"/>
        </g>
      </g>
    </svg>
  </section>
</body>
</html>
```